Coldbrook IT
Business Cards & Stationary
Hi everyone,
Thanks a lot for your efforts so far. Just a few pointers.
If possible leave a little white space somewhere on the business card incase someone wants to write on it. I write on business cards all the time.
I do prefer the dark background/light symbol. Also please try to incorporate the designed website address.
Thanks for your efforts so far and keep them coming!
Hi,
Please can you also provide samples of letterheaded paper and compliment slips as I would like the same theme carried through.
Thanks and keep up the good work!
Can you also try the dark background with the lighter symbol for the front of the business card.

```html
<!DOCTYPE html>
<html lang="en">
<head>
<meta charset="utf-8">
<title>Coldbrook IT — Stationery</title>
<link rel="stylesheet" href="https://fonts.googleapis.com/css2?family=Arimo:wght@400;700&display=swap">
<style>
  :root{
    --page:#ffffff;
    --frame:#d9d9d9;
    --band-top:#3a424b;
    --band-bottom:#22282e;
    --accent:#1f78c8;
    --accent-deep:#0d4d92;
    --paper:#ffffff;
    --ink:#3a3f45;
    --light-ink:#e6e9ec;
    --ghost:#e4e5e7;
  }
  *{box-sizing:border-box;margin:0;padding:0}
  html,body{width:1200px;height:738px;overflow:hidden;background:var(--page)}
  body{position:relative;font-family:"Arimo",Arial,sans-serif;color:var(--ink)}
  .board{position:absolute;inset:10px;border:1px solid var(--frame)}
  .sheet{position:absolute;background:var(--paper);box-shadow:2px 4px 10px rgba(0,0,0,.28)}
  .band{position:absolute;left:0;right:0;top:0;
    background:linear-gradient(180deg,var(--band-top),var(--band-bottom));
    border-bottom:4px solid var(--accent)}
  .brand{position:absolute;display:flex;align-items:center;gap:7px;
    color:var(--light-ink);font-weight:700;letter-spacing:.5px;white-space:nowrap}
  .brand-square{width:10px;height:10px;background:var(--light-ink)}
  .address{position:absolute;color:var(--light-ink);font-size:8px;line-height:10.5px}

  /* compliment slip */
  .comp-slip{left:72px;top:343px;width:542px;height:238px}
  .comp-slip .band{height:99px}
  .comp-slip .brand{left:20px;top:36px;font-size:19px}
  .comp-slip .address{left:377px;top:38px}
  .comp-slip .compliments{position:absolute;left:384px;top:182px;font-size:12px;letter-spacing:.3px;color:var(--ink)}

  /* letterhead */
  .letterhead{left:631px;top:77px;width:432px;height:607px}
  .letterhead .band{height:94px}
  .letterhead .brand{left:16px;top:36px;font-size:19px}
  .letterhead .address{left:247px;top:18px;font-size:7px;line-height:9.5px}
  .letterhead .ghost-mark{position:absolute;left:98px;top:395px;font-size:34px;font-weight:700;color:var(--ghost);white-space:nowrap}

  /* business cards */
  .card{left:967px;width:178px;height:106px}
  .card-front{top:329px}
  .card-front .band{height:52px;border-bottom-width:3px}
  .card-front .brand{left:10px;top:18px;font-size:12px;gap:5px}
  .card-front .brand-square{width:7px;height:7px}
  .card-front .holder{position:absolute;left:80px;top:64px;font-size:7px;line-height:9.5px;color:var(--ink)}
  .card-back{top:458px;background:radial-gradient(ellipse at center,var(--accent) 0%,var(--accent-deep) 100%)}
  .card-back .brand{left:50%;top:50%;transform:translate(-50%,-50%);font-size:15px;color:#ffffff}
  .card-back .brand-square{background:#ffffff}
</style>
</head>
<body>
  <div class="board"></div>

  <section class="sheet comp-slip" aria-label="Compliment slip">
    <div class="band">
      <div class="brand"><span class="brand-square"></span>Coldbrook IT</div>
      <p class="address">14 Harrow Square<br>Glenmoor, County Down, BT9 4LX</p>
    </div>
    <p class="compliments">WITH COMPLIMENTS</p>
  </section>

  <section class="sheet letterhead" aria-label="Letterhead">
    <div class="band">
      <div class="brand"><span class="brand-square"></span>Coldbrook IT</div>
      <p class="address">14 Harrow Square<br>Glenmoor, County Down, BT9 4LX<br>Tel: 028 9055 1234<br>Fax: 028 9055 1235<br>info@coldbrookit.com<br>www.coldbrookit.com</p>
    </div>
    <div class="ghost-mark">Coldbrook IT</div>
  </section>

  <section class="sheet card card-front" aria-label="Business card front">
    <div class="band">
      <div class="brand"><span class="brand-square"></span>Coldbrook IT</div>
    </div>
    <p class="holder">Aidan Morrow<br>Director</p>
  </section>

  <section class="sheet card card-back" aria-label="Business card back">
    <div class="brand"><span class="brand-square"></span>Coldbrook IT</div>
  </section>
</body>
</html>
```